Need sign/billboard help

I need somone to take my logo and turn it into a sign.
Needs to have: Bright Paws
Hound Play Lodge LLC
319-555-0187
Daycare - Boarding - Learning
Colors to use are in the pictures i included, however feel free to use different shades of gray. i Don't necessary want to background to be one solid color.
Also this sing will be a rectangle (4'x8')
Industry/Entity Type
Daycare
Look and feel
Each slider illustrates characteristics of the customer's brand and the style your logo design should communicate.

```html
<!DOCTYPE html>
<html lang="en">
<head>
<meta charset="utf-8">
<title>Bright Paws Billboard</title>
<link rel="stylesheet" href="https://fonts.googleapis.com/css2?family=Michroma&family=Montserrat:wght@500;700&family=Cinzel:wght@400&display=swap">
<style>
  :root {
    --lime: #a7cd38;
    --lime-soft: #c9e27a;
    --ink: #0d0d0d;
    --paper: #ffffff;
    --backdrop: #e9ebee;
  }
  * { margin: 0; padding: 0; box-sizing: border-box; }
  html, body { width: 1200px; height: 888px; overflow: hidden; background: var(--backdrop); }
  .billboard {
    position: absolute; left: 40px; top: 224px;
    width: 1120px; height: 440px;
    background: var(--paper);
    overflow: hidden;
    box-shadow: 0 6px 24px rgba(0,0,0,.18);
  }
  .header-bands { position: absolute; left: 0; top: 0; width: 1120px; height: 165px; }
  .brand-mark {
    position: absolute; left: 54px; top: 62px;
    display: flex; align-items: center; gap: 14px;
    font-family: "Michroma", sans-serif; font-size: 26px; color: var(--ink);
  }
  .brand-mark .dot { width: 30px; height: 30px; border-radius: 50%; background: var(--ink); }
  .contact {
    position: absolute; right: 36px; top: 30px; text-align: right; color: var(--paper);
    font-family: "Montserrat", sans-serif; font-weight: 700;
  }
  .contact .cta { font-size: 27px; letter-spacing: .5px; }
  .contact .phone { font-size: 50px; letter-spacing: 2px; margin-top: 6px; line-height: 1; }
  .title-block { position: absolute; left: 54px; top: 185px; }
  .business-name {
    font-family: "Michroma", sans-serif; font-size: 50px; letter-spacing: 6px;
    color: var(--ink); line-height: 1; text-transform: uppercase;
  }
  .business-entity {
    font-family: "Michroma", sans-serif; font-size: 20px; letter-spacing: 5px;
    color: var(--ink); text-transform: uppercase; margin-top: 10px;
  }
  .services {
    display: flex; align-items: center; gap: 22px; margin-top: 12px;
    font-family: "Cinzel", serif; font-size: 27px; color: var(--ink);
  }
  .services .bullet { width: 14px; height: 14px; border-radius: 50%; background: var(--lime); }
  .mascot-art {
    position: absolute; left: 770px; top: 172px; width: 300px; height: 180px;
    background: radial-gradient(ellipse at 55% 55%, var(--lime-soft), rgba(255,255,255,0) 70%);
  }
  .website {
    position: absolute; right: 36px; bottom: 54px; line-height: 1.2;
    font-family: "Montserrat", sans-serif; font-weight: 500; font-size: 19px; color: var(--ink);
  }
  .footer-band {
    position: absolute; left: 0; bottom: 0; width: 100%; height: 44px; background: var(--lime);
    display: flex; align-items: center; padding-left: 54px;
    font-family: "Montserrat", sans-serif; font-weight: 500; font-size: 18px; color: var(--ink);
  }
</style>
</head>
<body>
  <div class="billboard">
    <svg class="header-bands" viewBox="0 0 1120 165" aria-hidden="true">
      <rect x="0" y="0" width="1120" height="165" fill="var(--lime)"/>
      <polygon points="500,12 1120,12 1120,165 595,165" fill="var(--ink)"/>
    </svg>
    <div class="brand-mark"><span class="dot"></span><span>Bright Paws</span></div>
    <div class="contact">
      <div class="cta">Contact us Now</div>
      <div class="phone">319-555-0187</div>
    </div>

    <div class="title-block">
      <div class="business-name">Bright Paws</div>
      <div class="business-entity">Hound Play Lodge LLC</div>
      <div class="services">
        <span>Daycare</span><span class="bullet"></span>
        <span>Boarding</span><span class="bullet"></span>
        <span>Learning</span>
      </div>
    </div>

    <div class="mascot-art" role="img" aria-label="Lime green line illustration of a dog head in profile"></div>
    <div class="website">www.brightpawslodge.com</div>

    <div class="footer-band">E.mail-hello@brightpawslodge.com</div>
  </div>
</body>
</html>
```